Business card for a young aspring actress

My daughter is 18 and just starting out on her profession as an actress. She is a member of the Harbour Young Players and has already had some extras work and a featured role in an upcoming Feature film.

She wants/needs a card that she can have to hand to give to those she comes into contact with in the theatre, TV and film industries.

We are thinking that it may be double sided with an impact side including a picture of her and her name etc with the reverse holding contact and other details.

She wants to go by the name Maya Louise Brennick.

She has done a little modelling but sees herself as an actress.

She can be seen in this video
http://www.oakvalepark-academy.org/videos/be0881e4276ee2512c50a07f907c1d03?width=640&height=480

Target Market(s)

Anyone she comes into contact with in theatre TV and film industries.

Industry/Entity Type

Business

Requirements
Nice to have
• She has email and a website www.mayabrennick.com She is quite a connected girl

```html
<!DOCTYPE html>
<html lang="en">
<head>
<meta charset="utf-8">
<title>Maya Louise Brennick – Business Card</title>
<link href="https://fonts.googleapis.com/css2?family=Oxygen:wght@700&family=Questrial&family=Open+Sans:wght@400&display=swap" rel="stylesheet">
<style>
  :root {
    --stage: #5aa9dc;
    --card-dark: #1c1a22;
    --plum: #6a2a5e;
    --teal: #1f6f78;
    --amber: #a25a1c;
    --olive: #3b3a1e;
    --violet: #5a3a8a;
    --rose: #c0507a;
    --text-light: #f1eef4;
    --text-soft: #d9d4de;
    --rule: #b9b4bb;
    --icon-teal: #2aa6a8;
    --portrait-grey: #8c8c8c;
    --portrait-teal: #2b8a8c;
    --portrait-green: #6fb54a;
  }
  * { box-sizing: border-box; margin: 0; padding: 0; }
  html, body { width: 1200px; height: 675px; overflow: hidden; }
  body {
    background: var(--stage);
    position: relative;
  }
  .card {
    position: absolute;
    top: 184px;
    width: 560px;
    height: 306px;
    overflow: hidden;
    background:
      radial-gradient(circle at 12% 20%, rgba(150,50,120,.55), transparent 38%),
      radial-gradient(circle at 55% 30%, rgba(40,130,140,.55), transparent 40%),
      radial-gradient(circle at 85% 15%, rgba(60,90,60,.5), transparent 35%),
      radial-gradient(circle at 8% 90%, rgba(190,100,30,.6), transparent 35%),
      radial-gradient(circle at 45% 80%, rgba(140,50,110,.45), transparent 38%),
      radial-gradient(circle at 70% 70%, rgba(80,60,150,.45), transparent 35%),
      var(--card-dark);
  }
  .card--front { left: 30px; }
  .card--back { left: 610px; }

  /* front */
  .front__portrait {
    position: absolute;
    top: 17px; right: 20px;
    width: 99px; height: 118px;
    border: 2px solid #e9e9e9;
    background: linear-gradient(160deg, #d8d8d8, var(--portrait-grey) 60%, #4a4a4a);
  }
  .front__name {
    position: absolute;
    top: 70px; right: 130px;
    font-family: "Oxygen", sans-serif;
    font-weight: 700;
    font-size: 25px;
    letter-spacing: .3px;
    color: var(--text-light);
    text-transform: uppercase;
    white-space: nowrap;
  }
  .front__role {
    position: absolute;
    top: 112px; right: 130px;
    font-family: "Questrial", sans-serif;
    font-size: 17px;
    letter-spacing: 1.5px;
    color: var(--text-soft);
  }
  .front__panel {
    position: absolute;
    left: 0; right: 0;
    top: 143px; height: 116px;
    background: rgba(160,150,150,.38);
    border-top: 2px solid var(--rule);
    border-bottom: 2px solid var(--rule);
  }
  .front__web {
    position: absolute;
    right: 14px; bottom: 9px;
    font-family: "Questrial", sans-serif;
    font-size: 15px;
    letter-spacing: 1px;
    color: var(--text-soft);
    text-transform: uppercase;
  }

  /* back */
  .back__portrait {
    position: absolute;
    top: 0; right: 0;
    width: 230px; height: 100%;
    background:
      radial-gradient(ellipse at 60% 45%, rgba(111,181,74,.85), transparent 60%),
      linear-gradient(180deg, rgba(43,138,140,.3), var(--portrait-teal));
    -webkit-mask-image: linear-gradient(90deg, transparent, #000 40%);
    mask-image: linear-gradient(90deg, transparent, #000 40%);
  }
  .back__name {
    position: absolute;
    top: 32px; left: 140px;
    font-family: "Oxygen", sans-serif;
    font-weight: 700;
    font-size: 20px;
    color: var(--text-light);
    text-transform: uppercase;
    white-space: nowrap;
  }
  .back__role {
    position: absolute;
    top: 62px; left: 140px;
    font-family: "Questrial", sans-serif;
    font-size: 10px;
    letter-spacing: 1px;
    color: var(--text-soft);
  }
  .contacts {
    position: absolute;
    top: 140px; left: 40px;
    list-style: none;
    font-family: "Open Sans", sans-serif;
    font-size: 17px;
    color: var(--text-light);
  }
  .contacts li {
    display: flex;
    align-items: center;
    height: 27px;
  }
  .contact__icon {
    width: 20px; height: 20px;
    margin-right: 20px;
    border-radius: 4px;
    background: var(--icon-teal);
    color: #fff;
    font-family: "Open Sans", sans-serif;
    font-size: 14px;
    line-height: 20px;
    text-align: center;
  }
  .contact__icon--round { border-radius: 50%; }
</style>
</head>
<body>
  <section class="card card--front" aria-label="Card front">
    <div class="front__panel"></div>
    <div class="front__portrait" role="img" aria-label="Black and white portrait photo of the actress"></div>
    <h1 class="front__name">Maya Louise Brennick</h1>
    <p class="front__role">ACTRESS</p>
    <p class="front__web">www.mayabrennick.com</p>
  </section>

  <section class="card card--back" aria-label="Card back">
    <div class="back__portrait" role="img" aria-label="Colour-tinted portrait photo of the actress"></div>
    <h2 class="back__name">Maya Louise Brennick</h2>
    <p class="back__role">ACTRESS</p>
    <ul class="contacts">
      <li><span class="contact__icon">t</span>Telephone</li>
      <li><span class="contact__icon">e</span>E-mail</li>
      <li><span class="contact__icon">w</span>www.mayabrennick.com</li>
      <li><span class="contact__icon contact__icon--round"></span>Chirpline</li>
      <li><span class="contact__icon"></span>Friendwall</li>
    </ul>
  </section>
</body>
</html>
```